Stabilization Flyer

We are looking for a single document that outlines the info below - we want to emphasize that we can help child cares in the process and then we can help them make any award money go further through our program -
Don’t leave money on the table – as a child care owner you have access to grant money, but time is running out.

President Tallow signed the National Renewal Grant Act of 2021 (NRG). This plan includes $24 billion in child care stabilization grant funding. These funds will help keep early childhood educators and family child care providers keep their doors open and provide a critical step to paving the way for a strong economic recovery and a more equitable future.

Each State has its own application process – most licensed child care centers are eligible for grants with awards up to $400,000 per program. Awarded dollars is based upon your center’s capacity.

Grants are good for the following categories

Child care providers can use stabilization subgrants to cover these expenses:
• Wages and benefits, including increases in compensation for any staff.
• Rent, utilities, facilities maintenance and minor renovations, and insurance.
• Personal protective equipment, cleaning supplies, and other health and safety measures.
• Equipment and supplies used to respond to COVID-19.
• Material goods (i.e., to facilitate play or safe sleep) or services (i.e., food) used for the operation of the program. Yes, Food is an allowable expense.
• Mental health services for children and employees

If you have not applied for the grant, we can help point you in the right direction. Just email stablization@pantrycrateoutlet.com or call 877. 391.6052 and we will send you the links on how to file within your State. No purchase is necessary for this guidance, but we would love the opportunity to show you how we can stretch your purchases by up to 30%.

Target Market(s)

child care centers

Industry/Entity Type

child care is the target

Requirements
Must have
• website www.pantrycrateoutlet.com
Nice to have
• we have a video that could be embedded https://www.pantrycrateoutlet.com/video-resources/

```html
<!DOCTYPE html>
<html lang="en">
<head>
<meta charset="utf-8">
<title>Stabilization Flyer – Pantry Crate Outlet</title>
<link href="https://fonts.googleapis.com/css2?family=Montserrat:wght@400;500;600;700;800;900&family=Oswald:wght@500;600&display=swap" rel="stylesheet">
<style>
:root{
  --blue:#3a86cf;
  --blue-dark:#2e6fb3;
  --green:#8cc67a;
  --green-soft:#a7d596;
  --ink:#1d1d1f;
  --grey-text:#444;
  --footer-dark:#4a4a4a;
  --page:#ececec;
  --white:#fff;
}
*{box-sizing:border-box;margin:0;padding:0}
html,body{width:1200px;height:3382px;overflow:hidden;background:var(--page)}
body{font-family:'Montserrat',sans-serif;color:var(--ink);position:relative}
.flyer{position:absolute;left:30px;top:953px;width:1140px;height:1475px;background:var(--white);overflow:hidden}
.brand{position:absolute;left:82px;top:52px;display:flex;align-items:center;gap:14px}
.brand-mark{width:40px;height:40px;background:var(--green)}
.brand-name{font-size:38px;font-weight:500;color:var(--blue);letter-spacing:-0.5px}
.signed-band{position:absolute;left:0;top:161px;width:560px;height:124px;background:var(--blue);padding:12px 0 0 85px}
.signed-band h1{font-size:49px;line-height:52px;font-weight:900;color:var(--white);letter-spacing:0.5px}
.act-title{position:absolute;left:82px;top:300px;width:600px}
.act-title .line{display:block;font-weight:900;font-size:51px;line-height:54px;letter-spacing:0.2px;white-space:nowrap}
.act-title .blue{color:var(--blue)}
.act-title .green{color:var(--green)}
.act-title .year-line{font-family:'Oswald',sans-serif;font-weight:500;font-size:70px;line-height:80px;color:var(--ink);letter-spacing:-0.5px}
.act-title .year-line em{font-style:normal;color:var(--blue)}
.hero-photo{position:absolute;left:548px;top:-85px;width:600px;height:600px;border-radius:50%;border:12px solid #e4e4e4;overflow:hidden;background:radial-gradient(circle at 45% 40%,#f3dccb 0%,#c9a488 28%,#8fb2c9 55%,#e7c45c 75%,#d5d9de 100%)}
.grant-box{position:absolute;left:78px;top:535px;width:565px;height:212px;border:4px solid var(--blue);padding:4px}
.grant-box p{background:var(--green);height:100%;padding:18px 20px 0;color:var(--white);font-size:19.5px;line-height:24.6px;font-weight:500}
.grant-box strong{font-size:23px;font-weight:700}
.state-info{position:absolute;left:660px;top:570px;width:420px}
.state-info h2{font-size:20.5px;line-height:24px;font-weight:700;color:var(--blue)}
.state-detail{margin-top:8px;border-left:3px solid var(--green);padding-left:14px;position:relative}
.state-detail p{font-size:16.5px;line-height:21px;color:var(--grey-text)}
.state-detail .eligible{width:215px}
.state-detail .capacity{margin-top:14px}
.award-badge{position:absolute;left:225px;top:-6px;width:133px;height:72px;background:var(--blue);color:var(--white);text-align:center;padding-top:2px}
.award-badge b{display:block;font-family:'Oswald',sans-serif;font-weight:500;font-size:36px;line-height:42px}
.award-badge span{display:block;font-size:16px;line-height:20px}
.expenses{position:absolute;left:83px;top:812px;width:977px;height:300px;border:2px dashed var(--blue)}
.expenses h3{position:absolute;left:-4px;top:-20px;width:882px;margin-left:50px;height:48px;background:var(--blue);color:var(--white);border-radius:6px;font-size:21px;font-weight:600;text-align:center;line-height:48px}
.expense-list{list-style:none;position:absolute;top:45px;left:16px;right:10px;display:grid;grid-template-columns:436px 1fr;column-gap:30px}
.expense-list li{display:flex;gap:18px;font-size:17.5px;line-height:22px;color:var(--ink);margin-bottom:14px}
.expense-list .col{display:flex;flex-direction:column}
.icon{flex:0 0 auto;width:44px;height:44px;margin-top:2px}
.help-line{position:absolute;left:78px;top:1162px;width:982px;white-space:nowrap;font-size:22.5px;line-height:28px;font-weight:500;color:var(--ink)}
.contact-row{position:absolute;left:78px;top:1206px;width:982px;height:40px}
.contact-row .email-pill{position:absolute;left:290px;top:0;right:0;height:40px;background:var(--green);border-radius:20px;color:var(--white);font-size:27px;font-weight:500;line-height:40px;padding-left:10px;display:flex;align-items:center;gap:10px}
.contact-row .email-pill .or{font-weight:700}
.contact-row .phone{position:absolute;left:0;top:-2px;display:flex;align-items:center;gap:12px;background:var(--white);padding-right:12px;border-radius:0 22px 22px 0;height:44px;font-size:31px;font-weight:700;color:var(--blue)}
.offer{position:absolute;left:78px;top:1276px;width:982px;height:92px}
.offer p{position:absolute;left:0;top:0;width:660px;height:92px;border:2px solid var(--blue);padding:9px 8px;font-size:18px;line-height:24px;color:var(--ink)}
.offer .savings{position:absolute;right:0;top:0;width:330px;height:92px;background:var(--blue);color:var(--white);font-family:'Oswald',sans-serif;font-weight:500;font-size:60px;line-height:92px;text-align:center}
.offer .savings::before{content:"";position:absolute;left:-12px;top:34px;border-style:solid;border-width:12px 12px 12px 0;border-color:transparent var(--blue) transparent transparent}
.footer{position:absolute;left:0;bottom:0;width:1140px;height:78px}
.footer svg{position:absolute;inset:0}
.footer .video{position:absolute;left:78px;top:13px;color:var(--green-soft);font-size:17px;line-height:22px}
.footer .video a{color:var(--white);text-decoration:underline}
.footer .web{position:absolute;left:670px;top:0;height:78px;display:flex;align-items:center;gap:14px;color:var(--white);font-size:21px;font-weight:600}
</style>
</head>
<body>
<main class="flyer">
  <div class="brand"><span class="brand-mark"></span><span class="brand-name">Pantry Crate Outlet</span></div>

  <div class="hero-photo" role="img" aria-label="Photo of a teacher playing with building blocks alongside young children at a classroom table"></div>

  <div class="signed-band"><h1>PRESIDENT<br>TALLOW SIGNED</h1></div>

  <h2 class="act-title">
    <span class="line blue">THE NATIONAL</span>
    <span class="line green">RENEWAL GRANT</span>
    <span class="line year-line">ACT OF <em>2021</em> (NRG)</span>
  </h2>

  <div class="grant-box"><p>This plan includes <strong>$24 billion</strong> in child care stabilization grant funding. These funds will help keep early childhood educators and family child care providers keep their doors open and provide a critical step to paving the way for a strong economic recovery and a more equitable future.</p></div>

  <section class="state-info">
    <h2>Each State has its own application process</h2>
    <div class="state-detail">
      <p class="eligible">Most licensed child care centers are eligible for grants with awards up to</p>
      <div class="award-badge"><b>$400,000</b><span>per program.</span></div>
      <p class="capacity">Awarded dollars is based upon your center’s capacity.</p>
    </div>
  </section>

  <section class="expenses">
    <h3>Child care providers can use stabilization subgrants to cover these expenses:</h3>
    <div class="expense-list">
      <ul class="col">
        <li><svg class="icon" viewBox="0 0 44 44"><circle cx="22" cy="22" r="21" fill="#dcebd6"/><circle cx="22" cy="22" r="16" fill="var(--green)"/><circle cx="22" cy="22" r="7" fill="none" stroke="#fff" stroke-width="2"/></svg><span>Wages and benefits, including increases in compensation for any staff.</span></li>
        <li><svg class="icon" viewBox="0 0 44 44"><circle cx="22" cy="22" r="21" fill="#dcebd6"/><circle cx="22" cy="22" r="16" fill="var(--green)"/><path d="M22 13l7 3v6c0 5-3 8-7 9-4-1-7-4-7-9v-6z" fill="none" stroke="#fff" stroke-width="2"/></svg><span>Rent, utilities, facilities maintenance and minor renovations, and insurance.</span></li>
        <li><svg class="icon" viewBox="0 0 44 44"><circle cx="22" cy="22" r="21" fill="#dcebd6"/><circle cx="22" cy="22" r="16" fill="var(--green)"/><path d="M15 25h14M17 25v-6h10v6M20 19v-3h4v3" fill="none" stroke="#fff" stroke-width="2"/></svg><span>Personal protective equipment, cleaning supplies, and other health and safety measures.</span></li>
      </ul>
      <ul class="col">
        <li><svg class="icon" viewBox="0 0 44 44"><circle cx="22" cy="22" r="21" fill="#dcebd6"/><circle cx="22" cy="22" r="16" fill="var(--green)"/><rect x="15" y="15" width="14" height="14" fill="none" stroke="#fff" stroke-width="2"/></svg><span>Equipment and supplies used to respond to COVID-19.</span></li>
        <li><svg class="icon" viewBox="0 0 44 44"><circle cx="22" cy="22" r="21" fill="#dcebd6"/><circle cx="22" cy="22" r="16" fill="var(--green)"/><circle cx="18" cy="22" r="4" fill="none" stroke="#fff" stroke-width="2"/><circle cx="26" cy="22" r="4" fill="none" stroke="#fff" stroke-width="2"/></svg><span>Material goods (i.e., to facilitate play or safe sleep) or services (i.e., food) used for the operation of the program. Yes, Food is an allowable expense.</span></li>
        <li><svg class="icon" viewBox="0 0 44 44"><circle cx="22" cy="22" r="21" fill="#dcebd6"/><circle cx="22" cy="22" r="16" fill="var(--green)"/><path d="M22 30s-8-5-8-10a4 4 0 0 1 8-1 4 4 0 0 1 8 1c0 5-8 10-8 10z" fill="none" stroke="#fff" stroke-width="2"/></svg><span>Mental health services for children and employees</span></li>
      </ul>
    </div>
  </section>

  <p class="help-line">If you have not applied for the grant, we can help point you in the right direction.</p>

  <div class="contact-row">
    <div class="email-pill"><span class="or">or</span>
      <svg width="20" height="20" viewBox="0 0 20 20"><rect x="2" y="5" width="16" height="12" fill="#fff"/><path d="M2 5l8 6 8-6" fill="none" stroke="var(--green)" stroke-width="1.5"/></svg>
      <span>stablization@pantrycrateoutlet.com</span></div>
    <div class="phone">
      <svg width="40" height="40" viewBox="0 0 40 40"><circle cx="20" cy="20" r="18" fill="var(--blue)"/><circle cx="20" cy="20" r="14" fill="none" stroke="#fff" stroke-width="1.5"/><path d="M14 13c2-1 3 0 4 3l-2 2c1 2 3 4 5 5l2-2c3 1 4 2 3 4-1 2-3 2-5 1-4-2-7-5-9-9-1-2-1-3 2-4z" fill="#fff"/></svg>
      <span>877. 391.6052</span></div>
  </div>

  <div class="offer">
    <p>we will send you the links on how to file within your State. No purchase is necessary for this guidance, but we would love the opportunity to show you how we can stretch your purchases by</p>
    <div class="savings">Up to 30%</div>
  </div>

  <footer class="footer">
    <svg width="1140" height="78" viewBox="0 0 1140 78"><polygon points="0,0 640,0 595,78 0,78" fill="var(--footer-dark)"/><polygon points="648,0 1140,0 1140,78 603,78" fill="var(--green)"/></svg>
    <p class="video">Check out our video click link below:<br><a>https://www.pantrycrateoutlet.com/video-resources/</a></p>
    <div class="web"><svg width="30" height="30" viewBox="0 0 30 30"><circle cx="15" cy="15" r="13" fill="none" stroke="#fff" stroke-width="2"/><ellipse cx="15" cy="15" rx="6" ry="13" fill="none" stroke="#fff" stroke-width="1.5"/><path d="M2 15h26" stroke="#fff" stroke-width="1.5"/></svg><span>www.pantrycrateoutlet.com</span></div>
  </footer>
</main>
</body>
</html>
```